Executive Education Business needs a brochure for an IT Security workshop

UPDATE AND CLARIFICATION - I'm looking for a brochure that includes the text from the attached file "2014 IT Security Program Outline v2". This is a specific program we are putting on that we need a brochure designed for, using the content included in this file.

We have the basic text of a brochure, and need a design layout for a brochure that we can use to market this workshop to financial institutions in Asia and the Middle East. It may make sense to leave a spot on the cover somewhere to add a location and date (which we can edit based on program scheduling). Additionally, a registration page should be included either in the brochure or as an insert.

I'm attaching a brochure we used for a past program which provides an example registration page for our programs. I'm also including some photos from our programs that may be of use, although stock photography is also acceptable. Finally, I'm including two of our corporate brochures that may provide additional background on the company and our style.

```html
<!DOCTYPE html>
<html lang="en">
<head>
<meta charset="utf-8">
<title>IT Security Program Brochure</title>
<link href="https://fonts.googleapis.com/css2?family=Ubuntu:wght@400;500;700&family=Ubuntu+Condensed&display=swap" rel="stylesheet">
<style>
  :root {
    --crimson: #b8293f;
    --crimson-deep: #a1223a;
    --paper: #ececec;
    --paper-dark: #dedede;
    --ink: #2b2b2b;
    --white: #ffffff;
    --stage: #d4d4d4;
    --photo-dark: #1f2c3d;
    --photo-mid: #4c6078;
    --photo-light: #9fb0c2;
  }
  * { box-sizing: border-box; margin: 0; padding: 0; }
  html, body { width: 1200px; height: 824px; overflow: hidden; }
  body {
    background: var(--stage);
    font-family: "Ubuntu", Arial, sans-serif;
    color: var(--ink);
  }
  .spread {
    position: absolute; left: 60px; top: 40px;
    width: 1080px; height: 744px;
    display: flex;
    box-shadow: 0 6px 24px rgba(0,0,0,.18);
  }
  .page { width: 540px; height: 744px; display: flex; flex-direction: column; }

  /* Left page: registration */
  .registration { background: var(--paper); flex: 1; padding: 30px 30px 0 30px; font-size: 10.5px; line-height: 1.35; }
  .section-tag {
    display: inline-block; background: var(--crimson); color: var(--white);
    font-weight: 700; font-size: 13px; padding: 4px 16px; margin-bottom: 10px;
  }
  .program-facts p { margin-bottom: 1px; }
  .highlight { color: var(--crimson); font-weight: 700; }
  .program-facts .spaced { margin-top: 6px; }
  .form { margin-top: 18px; display: grid; grid-template-columns: auto 1fr auto 1fr; gap: 6px 6px; align-items: center; }
  .form label { font-size: 10.5px; white-space: nowrap; }
  .field { background: var(--white); height: 20px; }
  .span-3 { grid-column: span 3; }
  .submission { margin-top: 18px; }
  .submission p { margin-bottom: 8px; }
  .experience {
    background: var(--crimson); color: var(--white);
    height: 190px; padding: 22px 30px; font-size: 9.5px; line-height: 1.4;
  }
  .experience h2 { font-size: 12.5px; font-weight: 700; margin-bottom: 8px; }
  .experience p { margin-bottom: 9px; }

  /* Right page: cover */
  .masthead {
    background: var(--paper-dark); height: 56px;
    display: flex; align-items: center; justify-content: center; gap: 8px;
  }
  .brand-dot { width: 14px; height: 14px; border-radius: 50%; background: var(--crimson); }
  .brand-name { color: var(--crimson); font-size: 18px; font-weight: 400; }
  .hero {
    position: relative; height: 254px;
    background: linear-gradient(100deg, var(--photo-light) 0%, var(--photo-mid) 35%, var(--photo-dark) 70%);
  }
  .hero-title { position: absolute; left: 30px; top: 120px; }
  .hero-title h1 {
    font-family: "Ubuntu Condensed", "Arial Narrow", sans-serif;
    font-weight: 400; font-size: 38px; color: var(--crimson); line-height: 1;
  }
  .hero-title p {
    font-family: "Ubuntu Condensed", "Arial Narrow", sans-serif;
    font-size: 17px; color: var(--white); margin-top: 4px;
  }
  .divider { height: 14px; background: var(--paper-dark); }
  .overview {
    background: var(--crimson); color: var(--white); flex: 1;
    padding: 26px 34px; font-size: 10.5px; line-height: 1.4;
  }
  .overview ul { margin: 6px 0 12px 34px; }
  .overview li { margin-bottom: 1px; }
  .site-bar {
    background: var(--paper-dark); height: 58px;
    display: flex; align-items: center; justify-content: flex-end; gap: 8px;
    padding-right: 34px; color: var(--crimson); font-size: 13px;
  }
</style>
</head>
<body>
<main class="spread">
  <section class="page page-left">
    <div class="registration">
      <div class="section-tag">Registration Form</div>
      <div class="program-facts">
        <p>Program:</p>
        <p class="highlight">IT Security: Protecting the Integrity of your Technology Platforms</p>
        <p>Who should attend:</p>
        <p class="highlight">Senior IT professionals, including Chief Information Officers, direct reports, and others with responsibility for the security and reliability of vital technology platforms</p>
        <p class="spaced">Date : <span class="highlight">February 2014</span> | Venue: <span class="highlight">Grand Harbour Hotel, Manama, Bahrain</span></p>
        <p class="spaced">Fee: <span class="highlight">USD 950</span></p>
        <p class="highlight">Early Registration Discount: USD 850 until July 31.</p>
        <p class="highlight">Group Discount: USD 750 for additional participants from the same institution.</p>
      </div>
      <div class="form">
        <label>Name</label><div class="field span-3"></div>
        <label>Company</label><div class="field"></div><label>Contact Number</label><div class="field"></div>
        <label>Title</label><div class="field"></div><label>Email</label><div class="field"></div>
        <label>Fax Number</label><div class="field span-3"></div>
        <label>Professional certification and education</label><div class="field span-3"></div>
        <label>Name and title of direct supervisor</label><div class="field span-3"></div>
        <label>Secretary Name</label><div class="field span-3"></div>
        <label>Secretary Contact Number</label><div class="field span-3"></div>
        <label>Secretary Email</label><div class="field span-3"></div>
      </div>
      <div class="submission">
        <p>Completed forms may be faxed to <span class="highlight">+1-555-014-2270</span> or emailed to <span class="highlight">info@meridianexec.com</span> to secure a place in the program.</p>
        <p>Payment should be made within 30 days upon receipt of invoice to secure a place in the program, and must be made prior to the start of the program.</p>
      </div>
    </div>
    <div class="experience">
      <h2>Our Global Experience</h2>
      <p>Our instructors have deep experience educating executives in North America, the Middle East, and Asia. Our founder, Samir K. Haddad, was a Professor of Management Practice at Northbridge Business School and currently serves as Program Director of the Board Governance Education Program offered by the Regional Leadership and Governance Council in Malaysia.</p>
      <p>MIEL's clients include universities, multinational corporations, sovereign wealth funds, pension funds, and family businesses in Malaysia, China, Saudi Arabia, the United Arab Emirates, Kuwait, Bahrain, Canada, and the United States. Clients praise our courses and instructors for making challenging, difficult topics understandable and interesting.</p>
    </div>
  </section>

  <section class="page page-right">
    <header class="masthead">
      <span class="brand-dot"></span>
      <span class="brand-name">Meridian Institute of Executive Learning</span>
    </header>
    <div class="hero" role="img" aria-label="Photo of a businessman in a dark suit holding his hands around a cloud icon with a padlock">
      <div class="hero-title">
        <h1>IT SECURITY</h1>
        <p>Protecting the Integrity of your Technology Platforms</p>
      </div>
    </div>
    <div class="divider"></div>
    <div class="overview">
      <p>This one-day course, specifically designed for senior executives and IT professionals with direct responsibility for protecting the integrity of technology platforms, will enhance your understanding of the challenges faced by today's IT workforce. Key areas of discussion will include:</p>
      <ul>
        <li>Identifying unusual or unauthorized activity, breaches, or attempted access.</li>
        <li>Safeguards against outside intrusion.</li>
        <li>Building a framework of security controls and policies.</li>
        <li>Internal reporting and controls.</li>
        <li>Risks presented by embedded systems and mobile devices.</li>
        <li>Human resource considerations and reducing dependencies on individuals with key IT knowledge.</li>
        <li>Disaster recovery best practices, procedures, systems, and operating protocols.</li>
      </ul>
      <p>Mr. Samir K. Haddad, Chairman of Meridian Institute of Executive Learning, will lead a panel of experts with extensive industry experience in what promises to be a relevant and engaging program. In addition to learning from our senior faculty members, participants will be encouraged to share their own insights with the group about emerging best practices.</p>
    </div>
    <footer class="site-bar">
      <svg width="18" height="18" viewBox="0 0 18 18" aria-hidden="true">
        <g fill="none" stroke="#b8293f" stroke-width="1.4">
          <circle cx="9" cy="9" r="7.5"/>
          <ellipse cx="9" cy="9" rx="3.2" ry="7.5"/>
          <line x1="1.5" y1="9" x2="16.5" y2="9"/>
        </g>
      </svg>
      <span>www.MeridianExec.com</span>
    </footer>
  </section>
</main>
</body>
</html>
```